Funeral Services Site

We need a website for a Funeral Services company. The old website is: www.rouwcentrumdelvoort.be We need the same structure and text.

Target Market(s)

Customers.

Coding

Coded - Design and coding required

Number of Pages Required

4 page

Font styles to use
Serif
Sans Serif
Script

```html
<!DOCTYPE html>
<html lang="en">
<head>
<meta charset="utf-8">
<title>Funeral home Verhoeven</title>
<link href="https://fonts.googleapis.com/css2?family=Playfair+Display:wght@400;700&family=Roboto:wght@400;500&display=swap" rel="stylesheet">
<style>
:root{
  --ink:#4a4a4a;
  --text:#555;
  --coral:#e8a393;
  --blush:#fbd9d0;
  --sage:#7aae8b;
  --paper:#ececec;
  --footer:#515151;
  --white:#fff;
}
*{margin:0;padding:0;box-sizing:border-box}
html,body{width:1200px;height:2690px;overflow:hidden;background:var(--white)}
body{position:relative;font-family:'Roboto',sans-serif;color:var(--text)}
.abs{position:absolute}
.serif{font-family:'Playfair Display',serif}
/* header */
.brand{left:89px;top:14px;display:flex;align-items:center;gap:10px;font-family:'Playfair Display',serif;font-weight:700;font-size:20px;line-height:19px;color:#222}
.brand-mark{width:40px;height:40px;border-radius:50%;background:#222}
.nav{left:542px;top:30px;display:flex;gap:30px;font-size:13px;font-weight:500;color:#333;letter-spacing:.2px}
.nav .active{color:var(--coral)}
.lang{left:1061px;top:22px;height:26px;border-left:1px solid #ddd;padding-left:16px;padding-top:8px;font-size:13px;font-weight:500;color:#333}
/* buttons */
.btn{display:inline-flex;align-items:center;justify-content:center;width:137px;height:39px;font-size:14px;font-weight:500}
.btn-coral{background:var(--coral);color:var(--white)}
.btn-dark{background:var(--ink);color:var(--white)}
.btn-line{border:1px solid #333;color:#333;background:transparent}
/* hero */
.hero-title{left:87px;top:308px;font-family:'Playfair Display',serif;font-weight:700;font-size:60px;line-height:58px;color:var(--ink)}
.hero-sub{left:90px;top:434px;font-family:'Playfair Display',serif;font-size:24px;color:var(--ink)}
.hero-actions{left:89px;top:480px;display:flex;gap:7px}
.photo{display:block}
.slider-dots span{display:block;width:11px;height:11px;border-radius:50%;background:#bbb;margin-bottom:7px}
.slider-dots span:first-child{background:#555}
/* about */
.h2{font-family:'Playfair Display',serif;color:var(--ink);font-size:36px;line-height:40px}
.body-text{font-size:15px;line-height:24px;color:var(--text)}
.body-text p+p{margin-top:13px}
.checklist{list-style:none;font-size:15px;line-height:24px}
.checklist li{position:relative;padding-left:19px;margin-bottom:4px}
.checklist li::before{content:"";position:absolute;left:1px;top:9px;width:6px;height:6px;border-right:1.5px solid #999;border-top:1.5px solid #999;transform:rotate(45deg)}
/* cta */
.cta{left:0;top:1880px;width:1200px;height:415px;background:linear-gradient(180deg,#fff 0%,#f2f2f2 45%,#f4f4f4 100%)}
.cta-flowers{left:0;top:1880px;width:250px;height:415px;background:linear-gradient(160deg,#e3e6d8 0%,#f5e6e0 45%,#f2d6cf 100%)}
.cta-title{left:0;width:1200px;top:2020px;text-align:center;font-family:'Playfair Display',serif;font-size:40px;line-height:40px;color:var(--ink)}
.cta-sub{left:0;width:1200px;top:2110px;text-align:center;font-size:16px;color:#444}
.cta-actions{left:460px;top:2146px;display:flex;gap:7px}
/* footer */
.footer{left:0;top:2295px;width:1200px;height:395px;background:var(--footer);color:var(--white)}
.footer-brand{left:175px;top:2480px;display:flex;align-items:center;gap:10px;font-family:'Playfair Display',serif;font-weight:700;font-size:22px;color:var(--white)}
.footer-brand i{width:16px;height:16px;border-radius:50%;background:var(--white)}
.footer h3{font-size:19px;font-weight:500}
.footer-links{left:505px;top:2385px}
.footer-links ul{list-style:none;margin-top:14px;font-size:15px}
.footer-links li{height:32px}
.footer-contact{left:777px;top:2385px}
.contact-item{position:relative;padding-left:32px;margin-top:14px;font-size:15px;line-height:17px}
.contact-item b{font-family:'Playfair Display',serif;font-weight:700;font-size:15px;display:block}
.contact-item svg{position:absolute;left:0;top:4px}
.footer-rule{left:89px;top:2639px;width:1022px;height:1px;background:#6b6b6b}
.copyright{left:0;width:1200px;top:2656px;text-align:center;font-size:15px}
.to-top{left:1130px;top:2623px;width:32px;height:32px;border-radius:50%;background:var(--white)}
</style>
</head>
<body>

<header>
  <div class="abs brand"><span class="brand-mark"></span><span>Funeral home<br>Verhoeven</span></div>
  <nav class="abs nav">
    <span class="active">HOME</span><span>ABOUT US</span><span>CONDOLE ONLINE</span><span>ORDER FLOWERS</span><span>CONTACT</span>
  </nav>
  <div class="abs lang">EN &#709;</div>
</header>

<section class="hero">
  <h1 class="abs hero-title">Mourning center<br>Verhoeven bvba:</h1>
  <p class="abs hero-sub">condolences online via the website</p>
  <div class="abs hero-actions">
    <span class="btn btn-coral">011 63 27 40</span>
    <span class="btn btn-line">CONTACT US</span>
  </div>
  <svg class="abs" style="left:460px;top:150px" width="700" height="520" viewBox="460 150 700 520">
    <defs>
      <pattern id="dotgrid" width="14" height="14" patternUnits="userSpaceOnUse"><circle cx="3" cy="3" r="2.2" fill="#e2e2e2"/></pattern>
      <linearGradient id="heroPhoto" x1="0" y1="0" x2="1" y2="1">
        <stop offset="0" stop-color="#e9e6dc"/><stop offset=".45" stop-color="#c9b7a4"/><stop offset=".75" stop-color="#6f6a66"/><stop offset="1" stop-color="#3f4246"/>
      </linearGradient>
    </defs>
    <rect x="566" y="153" width="90" height="90" fill="var(--paper)"/>
    <rect x="900" y="162" width="160" height="130" fill="url(#dotgrid)"/>
    <rect x="945" y="429" width="161" height="185" fill="var(--sage)"/>
    <circle cx="557" cy="564" r="51" fill="var(--blush)"/>
    <circle cx="510" cy="621" r="14" fill="var(--blush)"/>
    <circle cx="832" cy="405" r="248" fill="url(#heroPhoto)" role="img" aria-label="Photo of a woman seen from behind carrying a large bouquet of white tulips"/>
    <rect x="591" y="695" width="18" height="30" rx="9" fill="none" stroke="#555" stroke-width="1.6"/>
  </svg>
  <div class="abs slider-dots" style="left:1150px;top:394px"><span></span><span></span><span></span></div>
  <svg class="abs" style="left:591px;top:695px" width="18" height="30"><rect x="1" y="1" width="16" height="28" rx="8" fill="none" stroke="#555" stroke-width="1.6"/><line x1="9" y1="7" x2="9" y2="12" stroke="#555" stroke-width="1.6"/></svg>
</section>

<section class="about">
  <div class="abs photo" style="left:320px;top:991px;width:207px;height:251px;background:linear-gradient(160deg,#8fb07a,#4f6d45 60%,#3a4a3c)" role="img" aria-label="Photo of flowers laid on a casket at a grave"></div>
  <div class="abs photo" style="left:137px;top:780px;width:338px;height:411px;background:linear-gradient(170deg,#bdb5ad 0%,#6b4a33 35%,#e7d8d6 70%,#8a6a55 100%);box-shadow:0 25px 40px rgba(0,0,0,.12)" role="img" aria-label="Photo of a pink and white bouquet on a wooden casket lid"></div>
  <h2 class="abs h2" style="left:592px;top:835px;width:520px;font-size:35px">Mourning center Verhoeven, a complete service in mourning and farewell guidance</h2>
  <h2 class="abs h2" style="left:587px;top:963px;font-weight:700;font-size:40px">About Us</h2>
  <div class="abs body-text" style="left:585px;top:1012px;width:480px">
    <p>Saying goodbye to a loved one is one of the toughest things in a life&shy;time. Funeral home Verhoeven in Lindeberg takes care of all the practical and administrative matters involved. So you can say goodbye in peace.</p>
    <p>Our people have a r uime experience in farewell guidance and stand for 24 hours at 24 hours for you. Our fully renovated funeral home is open to you and your acquaintances, so that you can greet your loved one at any time of the day.</p>
  </div>
</section>

<section class="organization">
  <div class="abs" style="left:752px;top:1384px;width:448px;height:501px;background:linear-gradient(180deg,#e4a293,#d99c8e 60%,#e9b2a5)"></div>
  <div class="abs photo" style="left:622px;top:1465px;width:242px;height:348px;background:linear-gradient(170deg,#e9e3dc,#c98a86 40%,#efe9e2 80%)" role="img" aria-label="Photo of a bridal style bouquet of roses"></div>
  <div class="abs photo" style="left:864px;top:1465px;width:241px;height:348px;background:linear-gradient(180deg,#2b211d,#4a2a22 45%,#a0654a 75%,#d8a77c)" role="img" aria-label="Photo of red memorial candles glowing"></div>
  <div class="abs photo" style="left:1105px;top:1465px;width:95px;height:348px;background:linear-gradient(160deg,#1a1a1a,#2a2a2a 40%,#cfc8bd 60%,#151515)" role="img" aria-label="Photo of an open prayer book with a white flower"></div>
  <h2 class="abs h2" style="left:139px;top:1407px;width:420px">Organization funeral and worship</h2>
  <div class="abs body-text" style="left:136px;top:1500px;width:446px;text-align:justify">
    <p>The organization of the funeral ceremony is a moment of reflec&shy;tion, where the personality of the deceased can be beautifully high&shy;lighted. Our team will assist you in this and select the most beauti&shy;ful texts, songs and photos with you in order to arrive at an appro&shy;priate and worthy goodbye.</p>
    <p style="margin-top:9px">The funeral can take place in your parish church or our auditori&shy;um if you wish, which can accommodate a maximum of 100 guests. We can arrange the following for you:</p>
  </div>
  <ul class="abs checklist" style="left:136px;top:1718px;width:440px">
    <li>Vigil the night before the funeral</li>
    <li>Prayer service with priest (if possible)</li>
    <li>Eucharistic celebration with priest (on Tuesday and Friday in the parishes of Lindeberg)</li>
  </ul>
</section>

<section>
  <div class="abs cta"></div>
  <div class="abs cta-flowers" role="img" aria-label="Photo of pale pink roses and greenery on white paper"></div>
  <h2 class="abs cta-title">Do you have any Questions Or would you<br>like to call in our Funeral Home?</h2>
  <p class="abs cta-sub">Contact us we are here for you.</p>
  <div class="abs cta-actions">
    <span class="btn btn-dark">011 63 27 40</span>
    <span class="btn btn-line">CONTACT US</span>
  </div>
</section>

<footer>
  <div class="abs footer"></div>
  <div class="abs footer-brand"><i></i>Funeral home Verhoeven</div>
  <div class="abs footer-links" style="color:#fff">
    <h3>USEFUL LINKS</h3>
    <ul><li>Home</li><li>About us</li><li>Condole online</li><li>Order flowers</li><li>Contact</li></ul>
  </div>
  <div class="abs footer-contact" style="color:#fff">
    <h3>CONTACT US</h3>
    <div class="contact-item">
      <svg width="20" height="14" viewBox="0 0 20 14"><rect x="0" y="0" width="20" height="14" fill="#cfcfcf"/><path d="M0 0 L10 8 L20 0" fill="none" stroke="#515151" stroke-width="1.5"/></svg>
      <b>Email</b>info@rouwcentrumverhoeven.be
    </div>
    <div class="contact-item" style="margin-top:16px">
      <svg width="18" height="18" viewBox="0 0 24 24"><path d="M6.6 10.8a15.1 15.1 0 0 0 6.6 6.6l2.2-2.2a1 1 0 0 1 1-.25 11.4 11.4 0 0 0 3.6.57 1 1 0 0 1 1 1V20a1 1 0 0 1-1 1A17 17 0 0 1 3 4a1 1 0 0 1 1-1h3.5a1 1 0 0 1 1 1c0 1.25.2 2.45.57 3.6a1 1 0 0 1-.25 1z" fill="#cfcfcf"/></svg>
      <b>24/24, 7 sur 7</b>011 63 27 40
    </div>
    <div class="contact-item" style="margin-top:16px">
      <svg width="16" height="22" viewBox="0 0 16 22"><path d="M8 0a8 8 0 0 0-8 8c0 6 8 14 8 14s8-8 8-14a8 8 0 0 0-8-8z" fill="#cfcfcf"/><circle cx="8" cy="8" r="3" fill="#515151"/></svg>
      <b>Bloesemstraat 18</b>3700 Heesveld (Lindeberg)
    </div>
  </div>
  <div class="abs footer-rule"></div>
  <p class="abs copyright" style="color:#fff">Copyright 2019 | All Right Reserved</p>
  <svg class="abs to-top" width="32" height="32" viewBox="0 0 32 32"><circle cx="16" cy="16" r="16" fill="#fff"/><path d="M12 18 L16 14 L20 18" fill="none" stroke="#555" stroke-width="1.5"/></svg>
</footer>

</body>
</html>
```